Chocolate covered bananas

“I am starting a new venture making chocolate coated frozen bananas. At start up I intend to have 4 different types:
3 will be single bananas ( Dark Chocolate, Dark chocolate with sprinkles and Dark Chocolate & Almonds) sold in individual packets, 70MM(W) x 215mm(L)

The other will be Banana Pops (smaller pieces of banana) sold in a 500g bag and then packed in a 165mm(L) x 50mm(W) X 165mm(H) cardboard box

The packaging will need my logo the wording “Chocolate Coated Frozen Banana” and the slogan “Crunchy Sunny Snack” on it. A picture of a Banana and Chocolate (The chocolate can be on the banana, getting poured on it, or even beside it).
I would like the words “Zero Trans-fat” on both the packaging (3 variations) and the 500g container along with “Healthy Dessert Treat” on the Container.

I need the Ingredients and nutritional information on the back"

one version can be submitted within the Contest period, however the winner is required to provide all 4 versions as part of the project.

Good Luck

JUST A QUICK NOTE THE BANANAS WILL BE ON A ICE-CREAM STICK AND THE BANANA POPS WILL BE ON A POPSICLE STICK.

Here are a couple of examples from places in America (no competition to me I am in another country) I'm am looking for something similar in size. as the packets in merrily mangoes and the cartons in corals kiwis. http://www.merrily-mangoes.example/products.php and http://www.coralskiwis.example/our-products/ I hope this helps Regards Gareth.

Hi I am getting some great designs Most are dark brown (or chocolate ) in colour they look good however most ice cream packs are dark and I think in order for these to stand out they need to be brighter with the chocolate as a secondary colour. Regards Gareth.

Hi all great designs it will be very hard to pick. just a quick note I made a spelling mistake in my brief it is HEALTHY DESSERT TREAT (NOT DESERT) SORRY Regards Gareth.

I would like to thank everyone for there time and effort they have put in to my packaging design contest. I am meeting with the packaging company on Thursday and will have a decision Thursday night. Regards Gareth.

Target Market(s)

I plan to go down the track that these are a healthy tasty fun treat.
I will be using real Bananas and Real chocolate.

```html
<!DOCTYPE html>
<html lang="en">
<head>
<meta charset="utf-8">
<title>Package Design – Concept 1</title>
<link rel="stylesheet" href="https://fonts.googleapis.com/css2?family=Delius&family=Pinyon+Script&family=Francois+One&family=Marcellus+SC&family=Libre+Baskerville:ital@1&family=Maven+Pro:wght@400;700&display=swap">
<style>
  :root {
    --paper: #ebe5db;
    --paper-light: #f4f0e8;
    --strip: #ffffff;
    --caption: #cbbfb0;
    --choc: #3a2119;
    --choc-deep: #27140d;
    --lime: #dedd2e;
    --lime-deep: #c9c71c;
    --sun: #f3e21c;
    --cream: #f1e9dc;
    --almond: #c9a766;
    --seal: #f3f2ee;
    --seal-ink: #6b6b6b;
  }
  html, body { margin: 0; padding: 0; overflow: hidden; }
  .board {
    position: relative;
    width: 1200px;
    height: 900px;
    overflow: hidden;
    background: radial-gradient(ellipse at 50% 40%, var(--paper-light), var(--paper) 70%);
  }
  .caption-strip {
    position: absolute;
    left: 0; top: 800px;
    width: 1200px; height: 100px;
    background: var(--strip);
  }
  .caption {
    position: absolute;
    left: 36px; top: 838px;
    margin: 0;
    font-family: "Maven Pro", sans-serif;
    font-weight: 400;
    font-size: 27px;
    letter-spacing: 1.5px;
    color: var(--caption);
  }
  .caption strong { font-weight: 700; }
  .defs { position: absolute; width: 0; height: 0; overflow: hidden; }
  .packet { position: absolute; display: block; filter: drop-shadow(0 2px 3px rgba(0,0,0,.18)); }
  .packet--small { top: 70px; width: 192px; height: 638px; }
  .packet--dark { left: 58px; }
  .packet--sprinkles { left: 294px; }
  .packet--almonds { left: 529px; }
  .packet--hero { left: 828px; top: 0; width: 287px; height: 900px; }

  .slogan { font-family: "Delius", cursive; fill: var(--sun); }
  .brand-name { font-family: "Marcellus SC", serif; fill: var(--sun); }
  .brand-line { font-family: "Marcellus SC", serif; fill: var(--sun); }
  .flavour-script { font-family: "Pinyon Script", cursive; fill: var(--cream); }
  .flavour-title { font-family: "Francois One", sans-serif; fill: #ffffff; letter-spacing: .5px; }
  .variant-script { font-family: "Pinyon Script", cursive; fill: var(--cream); }
  .variant-script--almond { fill: var(--almond); }
  .variant-small { font-family: "Libre Baskerville", serif; font-style: italic; fill: var(--cream); }
  .seal-text { font-family: "Marcellus SC", serif; fill: var(--seal-ink); }
  .footer-small { font-family: "Libre Baskerville", serif; font-style: italic; fill: var(--choc); }
  .footer-title { font-family: "Marcellus SC", serif; fill: var(--choc); }
</style>
</head>
<body>
<main class="board">

  <svg class="defs" aria-hidden="true">
    <defs>
      <linearGradient id="banana-tone" x1="0" y1="0" x2="1" y2="1">
        <stop offset="0" stop-color="#f7dc4a"/>
        <stop offset="1" stop-color="#e2b01f"/>
      </linearGradient>
      <linearGradient id="choc-tone" x1="0" y1="0" x2="1" y2="1">
        <stop offset="0" stop-color="#4a2a1d"/>
        <stop offset="1" stop-color="#24120b"/>
      </linearGradient>
      <linearGradient id="sheen" x1="0" y1="0" x2="1" y2="0">
        <stop offset="0" stop-color="#fff" stop-opacity="0"/>
        <stop offset=".25" stop-color="#fff" stop-opacity=".08"/>
        <stop offset=".4" stop-color="#fff" stop-opacity="0"/>
        <stop offset="1" stop-color="#000" stop-opacity=".12"/>
      </linearGradient>
      <radialGradient id="sprinkle-tone">
        <stop offset=".45" stop-color="#e2624a" stop-opacity="0"/>
        <stop offset=".6" stop-color="#e2624a" stop-opacity=".55"/>
        <stop offset=".78" stop-color="#8fc1e0" stop-opacity=".45"/>
        <stop offset="1" stop-color="#f0d23c" stop-opacity="0"/>
      </radialGradient>
      <linearGradient id="almond-tone" x1="0" y1="0" x2="1" y2="1">
        <stop offset="0" stop-color="#c68a52"/>
        <stop offset="1" stop-color="#8a5530"/>
      </linearGradient>

      <symbol id="pack-base" viewBox="0 0 192 638">
        <!-- body -->
        <rect class="pack-body" x="0" y="0" width="192" height="638" fill="var(--lime)"/>
        <path class="choc-pour" fill="var(--choc)"
          d="M0 0 H192 V352 C184 352 182 372 172 370 C162 368 166 350 150 352 C138 354 140 384 128 384 C116 384 120 356 104 356 C90 356 92 370 80 370 C68 370 70 350 56 350 C44 350 46 378 34 378 C22 378 24 356 12 356 C6 356 3 360 0 362 Z"/>
        <!-- crimp bands -->
        <rect x="0" y="0" width="192" height="14" fill="var(--choc-deep)"/>
        <path d="M0 4 H192 M0 8 H192 M0 12 H192" stroke="#000" stroke-opacity=".25" stroke-width=".8"/>
        <rect x="0" y="620" width="192" height="18" fill="var(--lime-deep)"/>
        <path d="M0 624 H192 M0 628 H192 M0 632 H192" stroke="#000" stroke-opacity=".12" stroke-width=".8"/>

        <!-- slogan -->
        <text class="slogan" x="96" y="92" font-size="15.5" text-anchor="middle">Crunchy Sunny Snack</text>
        <path d="M34 100 Q96 108 158 98" fill="none" stroke="var(--sun)" stroke-width="1.2"/>

        <!-- brand -->
        <circle cx="96" cy="140" r="20" fill="var(--sun)"/>
        <text class="brand-name" x="96" y="184" font-size="15" text-anchor="middle">Sunday Plantains</text>
        <text class="brand-line" x="96" y="198" font-size="7" text-anchor="middle" letter-spacing=".3">Chocolate Coated Frozen Bananas</text>

        <!-- flavour -->
        <text class="flavour-script" x="96" y="262" font-size="38" text-anchor="middle">Dark</text>
        <text class="flavour-title" x="96" y="300" font-size="31" text-anchor="middle" textLength="148" lengthAdjust="spacingAndGlyphs">CHOCOLATE</text>

        <!-- imagery -->
        <path role="img" aria-label="Bunch of ripe yellow bananas"
          d="M26 420 C40 384 120 380 158 402 C170 420 166 470 150 498 C110 520 52 512 30 482 C20 462 20 440 26 420 Z"
          fill="url(#banana-tone)"/>
        <path role="img" aria-label="Broken pieces of dark chocolate"
          d="M86 510 L140 478 L182 500 L182 558 L112 568 L86 548 Z"
          fill="url(#choc-tone)"/>

        <!-- zero trans-fat seal -->
        <circle cx="44" cy="512" r="30" fill="var(--seal)" stroke="#cfcfca" stroke-width="2" stroke-dasharray="2 2"/>
        <circle cx="44" cy="512" r="23" fill="none" stroke="var(--seal-ink)" stroke-width=".8"/>
        <text class="seal-text" x="44" y="498" font-size="7" text-anchor="middle">ZERO</text>
        <text class="seal-text" x="44" y="517" font-size="14" text-anchor="middle">0%</text>
        <text class="seal-text" x="44" y="530" font-size="6" text-anchor="middle">TRANS-FAT</text>

        <!-- footer -->
        <text class="footer-small" x="20" y="581" font-size="8">with real</text>
        <text class="footer-title" x="96" y="596" font-size="13.5" text-anchor="middle" textLength="162" lengthAdjust="spacingAndGlyphs">BANANAS &amp; CHOCOLATE</text>

        <!-- sheen -->
        <rect x="0" y="0" width="192" height="638" fill="url(#sheen)"/>
      </symbol>
    </defs>
  </svg>

  <svg class="packet packet--small packet--dark" viewBox="0 0 192 638" aria-label="Dark Chocolate packet">
    <use href="#pack-base"/>
  </svg>

  <svg class="packet packet--small packet--sprinkles" viewBox="0 0 192 638" aria-label="Dark Chocolate with Sprinkles packet">
    <use href="#pack-base"/>
    <circle role="img" aria-label="Scattered colourful sugar sprinkles" cx="96" cy="150" r="88" fill="url(#sprinkle-tone)"/>
    <text class="variant-script" x="96" y="332" font-size="24" text-anchor="middle">Sprinkles</text>
    <text class="variant-small" x="64" y="314" font-size="7">with</text>
  </svg>

  <svg class="packet packet--small packet--almonds" viewBox="0 0 192 638" aria-label="Dark Chocolate with Almonds packet">
    <use href="#pack-base"/>
    <text class="variant-small" x="120" y="313" font-size="7">with</text>
    <text class="variant-script variant-script--almond" x="92" y="332" font-size="25" text-anchor="middle">Almonds</text>
    <ellipse role="img" aria-label="Whole almonds with a green leaf" cx="148" cy="356" rx="26" ry="16" fill="url(#almond-tone)"/>
  </svg>

  <div class="caption-strip"></div>
  <p class="caption">PACKAGE DESIGN - <strong>CONCEPT 1.</strong> (mod. 1.)</p>

  <svg class="packet packet--hero" viewBox="0 0 192 638" preserveAspectRatio="xMidYMid slice" aria-label="Dark Chocolate packet, front view">
    <use href="#pack-base"/>
  </svg>

</main>
</body>
</html>
```